Wordpress Design Project (Tobwin)

We need a wordpress design for an established auction and real estate company based in Virginia. The winning design will incorporate the colors of logo (red and black) creatively with an accent color in a very professional and clean layout.

Industry/Entity Type

Real Estate

Requirements
Must have
• We will require winning designer to provide a layered PSD (Adobe photoshop) concept file, along with any non-standard font files used.

Horizontal Navigation menu with these links:
Home - Upcoming Auctions - Past Auctions - For Sale- Consignments - About Us - Highlights - Contact Us

A slideshow element on the home page using the placeholder image provided.

Sidebar widgets to be included are: Email sign-up form - Featured Auctions - Featured Assets for Sale (see attached for visual of these widgets)

attached logos in footer with company contact info

```html
<!DOCTYPE html>
<html lang="en">
<head>
<meta charset="utf-8">
<title>Tobwin Enterprises</title>
<link href="https://fonts.googleapis.com/css2?family=PT+Sans:wght@400;700&display=swap" rel="stylesheet">
<style>
:root{
  --red:#c8100f;
  --red-dark:#8e0b0a;
  --red-deep:#a50d0c;
  --ink:#1e1e1e;
  --text:#555;
  --muted:#888;
  --paper:#efefef;
  --white:#fff;
  --panel:#2b2b2b;
  --orange:#ef6a12;
  --field:#7a7a7a;
  --line:#ddd;
}
*{box-sizing:border-box;margin:0;padding:0}
html,body{width:691px;height:1200px;overflow:hidden;background:var(--paper)}
body{font-family:"PT Sans",Arial,sans-serif;color:var(--text);font-size:9px}
.page{position:relative;width:691px;height:1200px;overflow:hidden;
  background:linear-gradient(180deg,var(--red) 0,var(--red-deep) 218px,var(--paper) 218px)}
.abs{position:absolute}

/* header */
.brand{left:80px;top:6px;width:167px;height:49px;background:var(--white);border-radius:0 16px 0 0;display:flex;align-items:center;padding-left:13px;gap:8px}
.brand-mark{width:26px;height:26px;background:var(--red)}
.brand-name{font-weight:700;color:var(--ink);font-size:20px;line-height:18px}
.brand-name small{display:block;font-size:8px;letter-spacing:2px;line-height:9px}
.call{left:529px;top:13px;color:var(--white);font-size:11px}
.call strong{display:block;font-size:18px;font-weight:400;line-height:20px}
.rule{left:80px;top:55px;width:530px;height:3px;background:var(--white)}
.nav{left:80px;top:60px;width:530px;height:24px;display:flex;justify-content:space-between}
.nav a{color:var(--white);text-decoration:none;font-weight:700;font-size:10px;line-height:24px;padding:0 6px;white-space:nowrap}
.nav a.active{background:#2a0a0a;padding:0 13px}

/* slider */
.slider{left:82px;top:86px;width:528px;height:213px;border:2px solid var(--white);
  background:linear-gradient(180deg,#aecbe6 0,#dbe6ef 14%,#3c5b34 22%,#77a948 45%,#8fc05a 75%,#5b7a3e 100%)}
.slider-arrows{position:absolute;left:2px;bottom:2px;display:flex;gap:2px}
.slider-arrows span{width:16px;height:16px;background:rgba(0,0,0,.6);display:block}

/* headings */
.h{font-weight:700;color:var(--ink);font-size:11px;padding-bottom:4px;border-bottom:2px solid var(--red);white-space:nowrap}

/* login */
.login{left:80px;top:325px;width:114px;height:118px;background:var(--panel);padding:8px 11px;color:var(--white)}
.login h3{font-size:12px;margin-bottom:8px}
.field{height:16px;background:var(--field);border-radius:3px;margin-bottom:5px;font-size:8px;line-height:16px;padding-left:7px}
.login p{font-size:6.8px;margin:8px 0 6px;white-space:nowrap}
.login p span{color:#f6a21b}
.btn{display:inline-block;background:var(--orange);border-radius:3px;font-weight:700;font-size:8px;padding:3px 8px}

/* upcoming */
.upcoming{left:80px;top:458px;width:114px}
.up-item{display:flex;gap:5px;height:48px;padding-top:8px;border-bottom:1px solid var(--line)}
.date{flex:none;width:21px;height:33px;border:2px solid var(--red);background:var(--white);text-align:center;font-weight:700;color:var(--ink);font-size:6.5px;line-height:8px;padding-top:1px}
.date b{display:block;font-size:11px;line-height:12px}
.up-item h4{color:var(--red);font-size:8px}
.up-item p{font-size:7.5px;line-height:10px}
.promo{left:80px;top:687px;width:114px;height:135px;background:linear-gradient(180deg,#6f8c58,#b9a88a 60%,#3c3b30);display:flex;align-items:flex-end}
.promo div{background:rgba(0,0,0,.55);color:var(--white);font-size:7.5px;font-style:italic;padding:4px 3px;width:100%;line-height:10px}
.promo b{color:#6ad0f0}

/* featured auctions */
.featured{left:209px;top:323px;width:266px}
.card{position:absolute;left:0;width:266px;height:107px;background:var(--white);border:1px solid var(--line);padding:8px}
.card h4{color:var(--red);font-size:10px;font-weight:700}
.more{position:absolute;right:-2px;top:0;width:48px;height:19px;background:var(--red);color:var(--white);font-size:7px;font-weight:700;text-align:center;line-height:8px;padding-top:2px}
.thumb{position:absolute;left:12px;top:28px;width:72px;height:70px;background:linear-gradient(180deg,#c6cde0,#e6d9cf 40%,#7a9a4f 55%,#4e7530)}
.card-body{position:absolute;left:92px;top:27px;width:166px}
.card-body h5{color:var(--ink);font-size:8.5px}
.card-body p{font-size:7.5px;line-height:10px}
.meta{display:flex;gap:12px;margin-top:7px;background:#f3f3f3;padding:3px 6px;font-size:7.5px}
.meta b{color:var(--ink);font-size:8px}
.meta svg{vertical-align:-1px;margin-right:2px}

/* assets */
.assets{left:491px;top:323px;width:119px}
.asset{position:absolute;left:0;width:119px}
.asset p{font-size:8px;color:var(--text)}
.asset-img{position:relative;margin:4px 2px 0;width:115px;height:68px;border:2px solid var(--white);box-shadow:0 1px 2px rgba(0,0,0,.2);
  background:linear-gradient(180deg,#6d97c8,#e8eef4 40%,#8a9a7c 58%,#5e8a38)}
.sale{position:absolute;right:3px;top:0;width:12px;height:24px;background:var(--red);color:var(--white);font-size:5.5px;font-weight:700;writing-mode:vertical-rl;text-align:center}
.asset-btn{position:absolute;left:33px;bottom:-6px;background:#111;color:var(--white);font-size:6.5px;font-weight:700;padding:2px 7px;white-space:nowrap}

/* clients */
.divider{left:80px;top:858px;width:530px;height:1px;background:var(--line)}
.clients-tag{left:283px;top:846px;width:126px;height:24px}
.clients-tag span{position:absolute;left:0;top:0;width:126px;text-align:center;line-height:24px;color:var(--white);font-weight:700;font-size:13px}
.client{top:885px;width:92px;height:55px;background:var(--white);box-shadow:0 3px 4px rgba(0,0,0,.12);display:flex;align-items:center;justify-content:center;text-align:center;font-weight:700;color:var(--ink);font-size:9px;padding:0 6px}
.viewmore{left:300px;top:958px;width:91px;text-align:center;color:var(--muted);font-size:8px}

/* footer */
.crowd{left:477px;top:989px;width:133px;height:48px;background:var(--red)}
.footer{left:0;top:1037px;width:691px;height:163px;background:linear-gradient(180deg,var(--red),var(--red-dark));color:var(--white)}
.fcol{position:absolute;top:12px;font-size:8px;line-height:11.5px;white-space:nowrap}
.fcol h4{font-size:9.5px;margin-bottom:8px}
.social{display:flex;gap:8px;font-weight:700;font-size:8px}
.flogo{position:absolute;left:283px;top:90px;display:flex;align-items:center;gap:6px;color:rgba(255,255,255,.7);font-weight:700;font-size:20px;line-height:18px}
.flogo i{width:24px;height:24px;background:rgba(255,255,255,.5)}
.flogo small{display:block;font-size:8px;letter-spacing:2px;line-height:9px}
.copy{position:absolute;left:0;top:143px;width:691px;text-align:center;font-size:7px}
</style>
</head>
<body>
<div class="page">
  <div class="abs brand"><span class="brand-mark"></span><div class="brand-name">Tobwin<small>ENTERPRISES</small></div></div>
  <div class="abs call">Call us on<strong>9850012347</strong></div>
  <div class="abs rule"></div>
  <nav class="abs nav">
    <a class="active">Home</a><a>Upcoming Auction</a><a>Past Auction</a><a>For Sale</a><a>Consignments</a><a>About Us</a><a>Highlights</a><a>Contact Us</a>
  </nav>
  <div class="abs slider" role="img" aria-label="Slideshow photo of green rolling hills with a wind turbine and farm buildings">
    <div class="slider-arrows"><span></span><span></span></div>
  </div>

  <div class="abs login">
    <h3>Log In</h3>
    <div class="field">Email</div>
    <div class="field">Password</div>
    <p>Forget your password? <span>Sign up</span></p>
    <span class="btn">Sign in</span>
  </div>

  <section class="abs upcoming">
    <div class="h">Upcoming Auction</div>
    <div class="up-item"><div class="date">TUE<b>09</b>APR</div><div><h4>Lorem Ipsum</h4><p>Proin gravida nibh vel velit auctor aliquet...</p></div></div>
    <div class="up-item"><div class="date">TUE<b>09</b>APR</div><div><h4>Lorem Ipsum</h4><p>Proin gravida nibh vel velit auctor aliquet...</p></div></div>
    <div class="up-item"><div class="date">TUE<b>09</b>APR</div><div><h4>Lorem Ipsum</h4><p>Proin gravida nibh vel velit auctor aliquet...</p></div></div>
    <div class="up-item"><div class="date">TUE<b>09</b>APR</div><div><h4>Lorem Ipsum</h4><p>Proin gravida nibh vel velit auctor aliquet...</p></div></div>
  </section>
  <div class="abs promo" role="img" aria-label="Photo of a family in front of their house"><div>We help our clients make <b>BETTER DECISION IN REAL ESTATE</b></div></div>

  <section class="abs featured">
    <div class="h">Featured Auction</div>
    <article class="card" style="top:28px"><h4>Proin gravida nibh velit auctor aliquet.</h4><span class="more">View More Details</span><div class="thumb" role="img" aria-label="Farmland photo"></div><div class="card-body"><h5>Details</h5><p>Lorem Ipsum. Proin gravida nibh vel velit auctor aliquet. Aenean sollicitudin, lorem quis bibendum auctor, nisi elit consequat ipsum,</p><div class="meta"><div><svg width="7" height="7" viewBox="0 0 8 8"><circle cx="4" cy="4" r="3" fill="none" stroke="#c8100f" stroke-width="1.2"/><path d="M4 2v2h1.5" stroke="#c8100f" fill="none"/></svg><b>Time</b><br>11 am to 1:00 pm</div><div><svg width="6" height="8" viewBox="0 0 6 8"><path d="M3 8C1 5 0 4 0 3a3 3 0 0 1 6 0c0 1-1 2-3 5z" fill="#c8100f"/></svg><b>Location</b><br>Area Name , Place Name</div></div></div></article>
    <article class="card" style="top:151px"><h4>Proin gravida nibh velit auctor aliquet.</h4><span class="more">View More Details</span><div class="thumb" role="img" aria-label="Farmland photo"></div><div class="card-body"><h5>Details</h5><p>Lorem Ipsum. Proin gravida nibh vel velit auctor aliquet. Aenean sollicitudin, lorem quis bibendum auctor, nisi elit consequat ipsum,</p><div class="meta"><div><svg width="7" height="7" viewBox="0 0 8 8"><circle cx="4" cy="4" r="3" fill="none" stroke="#c8100f" stroke-width="1.2"/><path d="M4 2v2h1.5" stroke="#c8100f" fill="none"/></svg><b>Time</b><br>11 am to 1:00 pm</div><div><svg width="6" height="8" viewBox="0 0 6 8"><path d="M3 8C1 5 0 4 0 3a3 3 0 0 1 6 0c0 1-1 2-3 5z" fill="#c8100f"/></svg><b>Location</b><br>Area Name , Place Name</div></div></div></article>
    <article class="card" style="top:273px"><h4>Proin gravida nibh velit auctor aliquet.</h4><span class="more">View More Details</span><div class="thumb" role="img" aria-label="Farmland photo"></div><div class="card-body"><h5>Details</h5><p>Lorem Ipsum. Proin gravida nibh vel velit auctor aliquet. Aenean sollicitudin, lorem quis bibendum auctor, nisi elit consequat ipsum,</p><div class="meta"><div><svg width="7" height="7" viewBox="0 0 8 8"><circle cx="4" cy="4" r="3" fill="none" stroke="#c8100f" stroke-width="1.2"/><path d="M4 2v2h1.5" stroke="#c8100f" fill="none"/></svg><b>Time</b><br>11 am to 1:00 pm</div><div><svg width="6" height="8" viewBox="0 0 6 8"><path d="M3 8C1 5 0 4 0 3a3 3 0 0 1 6 0c0 1-1 2-3 5z" fill="#c8100f"/></svg><b>Location</b><br>Area Name , Place Name</div></div></div></article>
    <article class="card" style="top:395px"><h4>Proin gravida nibh velit auctor aliquet.</h4><span class="more">View More Details</span><div class="thumb" role="img" aria-label="Farmland photo"></div><div class="card-body"><h5>Details</h5><p>Lorem Ipsum. Proin gravida nibh vel velit auctor aliquet. Aenean sollicitudin, lorem quis bibendum auctor, nisi elit consequat ipsum,</p><div class="meta"><div><svg width="7" height="7" viewBox="0 0 8 8"><circle cx="4" cy="4" r="3" fill="none" stroke="#c8100f" stroke-width="1.2"/><path d="M4 2v2h1.5" stroke="#c8100f" fill="none"/></svg><b>Time</b><br>11 am to 1:00 pm</div><div><svg width="6" height="8" viewBox="0 0 6 8"><path d="M3 8C1 5 0 4 0 3a3 3 0 0 1 6 0c0 1-1 2-3 5z" fill="#c8100f"/></svg><b>Location</b><br>Area Name , Place Name</div></div></div></article>
  </section>

  <section class="abs assets">
    <div class="h">Featured Assets For Sale</div>
    <div class="asset" style="top:26px"><p>Aenean sollicitudin, lorem</p><div class="asset-img" role="img" aria-label="Photo of a farm property under a cloudy sky"><span class="sale">SALE</span><span class="asset-btn">VIEW MORE</span></div></div>
    <div class="asset" style="top:125px"><p>Aenean sollicitudin, lorem</p><div class="asset-img" role="img" aria-label="Photo of a farm property under a cloudy sky"><span class="sale">SALE</span><span class="asset-btn">VIEW MORE</span></div></div>
    <div class="asset" style="top:224px"><p>Aenean sollicitudin, lorem</p><div class="asset-img" role="img" aria-label="Photo of a farm property under a cloudy sky"><span class="sale">SALE</span><span class="asset-btn">VIEW MORE</span></div></div>
    <div class="asset" style="top:323px"><p>Aenean sollicitudin, lorem</p><div class="asset-img" role="img" aria-label="Photo of a farm property under a cloudy sky"><span class="sale">SALE</span><span class="asset-btn">VIEW MORE</span></div></div>
    <div class="asset" style="top:422px"><p>Aenean sollicitudin, lorem</p><div class="asset-img" role="img" aria-label="Photo of a farm property under a cloudy sky"><span class="sale">SALE</span><span class="asset-btn">VIEW MORE</span></div></div>
  </section>

  <div class="abs divider"></div>
  <div class="abs clients-tag">
    <svg width="126" height="24" viewBox="0 0 126 24"><path d="M0 0h126l-10 12 10 12H0l10-12z" fill="#222"/></svg>
    <span>Our Clients</span>
  </div>
  <div class="abs client" style="left:80px">Harlow Auction Guild</div>
  <div class="abs client" style="left:190px">Brenton Bidders</div>
  <div class="abs client" style="left:299px">Ashby Sale Circle</div>
  <div class="abs client" style="left:408px">Corvel Auction Society</div>
  <div class="abs client" style="left:518px">Quellan Racing</div>
  <div class="abs viewmore">—— View More ——</div>

  <div class="abs crowd" role="img" aria-label="Silhouettes of people gathered at an auction"></div>
  <footer class="abs footer">
    <div class="fcol" style="left:80px"><h4>Contact</h4>house no, Area name,<br>street anme, state name,<br>country name.</div>
    <div class="fcol" style="left:207px"><h4>Phone no</h4>9850016620<br>9950017731</div>
    <div class="fcol" style="left:319px"><h4>Quick links</h4>Home<br>Upcoming Auction<br>Past Auction<br>For Sale</div>
    <div class="fcol" style="left:419px"><h4>&nbsp;</h4>Consignments<br>About Us<br>Highlights<br>Contact Us</div>
    <div class="fcol" style="left:517px"><h4>Follow us</h4><div class="social"><span>Linkora</span><span>Facely</span><span>Chirpa</span></div></div>
    <div class="flogo"><i></i><div>Tobwin<small>ENTERPRISES</small></div></div>
    <div class="copy">© 2013 Tobwin Enterprises. All Rights Reserved | Privacy Statement</div>
  </footer>
</div>
</body>
</html>
```